New CD - "Tunes About Marla" (Jazz piano standards)

We need a CD design for album of jazz piano standards. The music is elegant, fun, and artistic. Appeals to all lovers of Halvorsen, Brenton, Dubrow, etc. Includes Red Harbor, Can't Stop Dancin', Harbor Serenade, She Keeps A Secret In Her Pocket, Rain Falls On Quiet Streets, Lazy Tuesday, (Tonight) Across The Meadow, Hours by Candle and Lace, When Rivers Bend, Only If You Call, Your Quiet Spark, She Always Left The Door, Remarkable Dawn, Prelude Op. 28, No. 15 "Lamplight"/T. Varga.

Target Market(s)

Anyone who likes piano music.

```html
<!DOCTYPE html>
<html lang="en">
<head>
<meta charset="utf-8">
<title>Desmond Albright — Tunes About Marla</title>
<link rel="stylesheet" href="https://fonts.googleapis.com/css2?family=Cinzel:wght@400;500;600&display=swap">
<style>
  :root {
    --bg-grey: #959394;
    --bg-haze: #a7a6a8;
    --globe-amber: #d8812f;
    --globe-rust: #8a3f12;
    --globe-umber: #3a2416;
    --globe-slate: #5d5a5c;
    --title-white: #fbf8f4;
    --subtitle-rust: #7a2c12;
  }
  html, body {
    margin: 0;
    padding: 0;
    width: 1200px;
    height: 1200px;
    overflow: hidden;
  }
  .cover {
    position: relative;
    width: 1200px;
    height: 1200px;
    background:
      radial-gradient(circle at 52% 47%, var(--bg-haze) 0%, var(--bg-grey) 62%);
    font-family: "Cinzel", serif;
  }
  .cover__globe {
    position: absolute;
    left: 150px;
    top: 125px;
    width: 880px;
    height: 880px;
  }
  .cover__artist {
    position: absolute;
    left: 0;
    right: 0;
    top: 1022px;
    margin: 0;
    padding-left: 56px;
    text-align: center;
    font-weight: 500;
    font-size: 42px;
    letter-spacing: 3px;
    color: var(--title-white);
  }
  .cover__album {
    position: absolute;
    left: 0;
    right: 0;
    top: 1098px;
    margin: 0;
    padding-left: 56px;
    text-align: center;
    font-weight: 500;
    font-size: 24px;
    letter-spacing: 5px;
    text-transform: lowercase;
    font-variant: small-caps;
    color: var(--subtitle-rust);
  }
</style>
</head>
<body>
  <main class="cover">
    <svg class="cover__globe" viewBox="0 0 880 880" role="img"
         aria-label="Tiny-planet panorama photograph of a garden with bare trees and houses at sunset, warm amber on the left fading to dusky grey on the right">
      <defs>
        <linearGradient id="globeTone" x1="0" y1="0" x2="1" y2="0">
          <stop offset="0" stop-color="var(--globe-amber)"/>
          <stop offset="0.45" stop-color="var(--globe-rust)"/>
          <stop offset="0.62" stop-color="var(--globe-umber)"/>
          <stop offset="1" stop-color="var(--globe-slate)"/>
        </linearGradient>
        <radialGradient id="globeEdge" cx="0.5" cy="0.5" r="0.5">
          <stop offset="0.82" stop-color="#000" stop-opacity="0"/>
          <stop offset="1" stop-color="#959394" stop-opacity="0.85"/>
        </radialGradient>
      </defs>
      <circle cx="458" cy="436" r="400" fill="url(#globeTone)"/>
      <circle cx="458" cy="436" r="400" fill="url(#globeEdge)"/>
    </svg>

    <h1 class="cover__artist">Desmond Albright</h1>
    <p class="cover__album">Tunes About Marla</p>
  </main>
</body>
</html>
```